Kindle the Quiet Summit is a guide to help individuals overcome obstacles that they face in their life. This book provides thought provoking concepts that allow individuals to work through challenges if their life. The cover needs to be powerful! It needs to speak to the reader of breaking free of problems and overcoming challenges.

Kindle The Quiet Summit
A Handbook for climbing past hardships and growing into the self you were destined to become.
By
Dr. Marcus J. Belcroft

```html
<!DOCTYPE html>
<html lang="en">
<head>
<meta charset="utf-8">
<title>Kindle The Quiet Summit – Book Cover</title>
<link rel="stylesheet" href="https://fonts.googleapis.com/css2?family=Cinzel:wght@700&family=Crimson+Text:wght@600;700&display=swap">
<style>
  :root {
    --page-bg: #ececec;
    --title-white: #ffffff;
    --subtitle-brown: #5a1c0c;
    --spine-brown: #6e3c1e;
    --spine-edge: #8a5430;
    --band-grey: #8d8883;
    --band-grey-light: #a29d98;
    --author-ink: #2e2520;
    --sky-top: #3a1c10;
    --sky-mid: #b8601c;
    --sky-glow: #f2b040;
    --sky-low: #2a140c;
  }
  html, body {
    margin: 0;
    padding: 0;
    width: 1200px;
    height: 1200px;
    overflow: hidden;
    background: var(--page-bg);
  }
  .canvas {
    position: relative;
    width: 1200px;
    height: 1200px;
  }
  .cover-wrap {
    position: absolute;
    left: 60px;
    top: 208px;
    width: 1080px;
    height: 784px;
    overflow: hidden;
    box-shadow: 0 6px 24px rgba(0,0,0,0.25);
  }
  .cover-photo {
    position: absolute;
    inset: 0;
    background:
      radial-gradient(ellipse 40% 35% at 74% 62%, rgba(255,226,140,0.85), rgba(242,176,64,0) 100%),
      linear-gradient(180deg, var(--sky-top) 0%, var(--sky-mid) 40%, var(--sky-glow) 62%, var(--sky-low) 100%);
  }
  .spine {
    position: absolute;
    left: 521px;
    top: 0;
    width: 36px;
    height: 100%;
    background: var(--spine-brown);
    border-left: 2px solid var(--spine-edge);
    border-right: 2px solid var(--spine-edge);
    box-sizing: border-box;
  }
  .spine-title {
    position: absolute;
    left: 50%;
    top: 40px;
    transform-origin: 0 0;
    transform: rotate(90deg) translate(0, -50%);
    white-space: nowrap;
    font-family: "Crimson Text", serif;
    font-weight: 600;
    font-size: 19px;
    letter-spacing: 1.5px;
    color: var(--title-white);
    text-transform: uppercase;
  }
  .front-title {
    position: absolute;
    left: 600px;
    top: 40px;
    margin: 0;
    font-family: "Cinzel", serif;
    font-weight: 700;
    color: var(--title-white);
    line-height: 1.08;
    font-size: 54px;
    text-shadow: 0 2px 6px rgba(60,20,0,0.35);
  }
  .front-title .line { display: block; }
  .front-title .cap { font-size: 72px; }
  .subtitle {
    position: absolute;
    left: 600px;
    top: 372px;
    width: 250px;
    margin: 0;
    font-family: "Crimson Text", serif;
    font-weight: 700;
    font-size: 22px;
    line-height: 1.3;
    color: var(--subtitle-brown);
  }
  .author-band {
    position: absolute;
    left: 557px;
    right: 0;
    top: 728px;
    height: 24px;
    background: linear-gradient(var(--band-grey-light), var(--band-grey));
  }
  .author {
    margin: 0;
    line-height: 24px;
    text-align: center;
    font-family: "Crimson Text", serif;
    font-weight: 600;
    font-size: 16px;
    color: var(--author-ink);
  }
</style>
</head>
<body>
<div class="canvas">
  <div class="cover-wrap">
    <div class="cover-photo" role="img" aria-label="Photograph of a climber silhouetted on a rock face against a golden sunset sky with clouds and distant mountains"></div>

    <div class="spine">
      <span class="spine-title">Kindle The Quiet Summit</span>
    </div>

    <h1 class="front-title">
      <span class="line"><span class="cap">K</span>INDLE</span>
      <span class="line">THE QUIET</span>
      <span class="line"><span class="cap">S</span>UMMIT</span>
    </h1>

    <p class="subtitle">A Handbook for climbing past hardships and growing into the self you were destined to become.</p>

    <div class="author-band">
      <p class="author">Dr. Marcus J. Belcroft</p>
    </div>
  </div>
</div>
</body>
</html>
```